Lumora.io Homepage Redesign

We are seeking a talented designer to create an emotive and aspirational homepage for our website (www.lumora.io) that elevates the Lumora.io brand using our new home page copy.

Our current design feels product-heavy and lacks the global, professional, and emotive touch we're aiming for.

We want to strip back unnecessary visual distractions and focus on a more streamlined, compelling design that resonates with our audience.

Project Goals:
Replace product-heavy, literal imagery with more evocative, aspirational visuals.
Create a homepage that feels aspirational and professional, reflecting our global ambitions.
Explore the use of icons or simple graphics to reduce visual clutter and create a more refined experience.
Ensure that usability principles are at the forefront of the design. Navigation must be clear and accessible on both desktop and mobile.
Practicality is key. Any animations or transitions should serve a functional purpose and should not hinder website speed or performance.
We prefer mockups in Adobe XD for ease of use by our developer, but Photoshop is also acceptable if this suits your workflow better.

Design Considerations:
Imagery: The selected imagery should enhance the emotive feel of the site, not simply fill space.
Usability: Avoid hidden navigation on desktop, and ensure key call-to-action buttons like "Watch Demo" and "Book a Demo" are clearly identifiable as clickable.
Animations/Transitions: Any animated elements should focus on showcasing our content, not just adding visual flair. Consider website performance and practicality in your design.
Content Hierarchy: Follow the suggested hierarchy based on provided copy, giving prominence to our key propositions while minimizing distractions.
Style: Maintain Lumora.io's colour scheme and font set, but we welcome fresh perspectives on how to apply them.
Copy: We will be providing new written copy to replace the current content on the website. The new design should complement and elevate the revised messaging.

Deliverables:
An initial homepage mock-up based on our brand guidelines.
Two rounds of feedback and revisions based on our input.
Final design files provided in Adobe XD (preferred) or Photoshop.

Brand Resources:
You will be given access to our Adobe Library, Brand Guidelines, and new website copy (and indicative wireframe), along with any necessary imagery from our stock library.
Note: please contact us if you would like access to our Adobe Library.

Number of Pages Required

1 page

Font styles to use
Sans Serif
Other font styles liked:
• Poppins Bold, Proxima Nova Light, Bold.

Colors

Designer to choose colors to be used in the design.

Requirements
Must have
• New website copy as supplied and ideally follow the wireframe provided. Aspirational visuals. Meets our brand guidelines
Should not have
• Stock standard imagery.

```html
<!DOCTYPE html>
<html lang="en">
<head>
<meta charset="utf-8">
<title>Lumora.io — Homepage</title>
<link href="https://fonts.googleapis.com/css2?family=Poppins:wght@300;400;500;600;700&display=swap" rel="stylesheet">
<style>
:root{
  --red:#c8102e;
  --red-deep:#8a0b17;
  --red-mid:#a90d1f;
  --green:#9cc43c;
  --yellow:#f5c518;
  --lime:#c9d22e;
  --navy:#1b2136;
  --ink:#222633;
  --grey:#6b6f7a;
  --silver:#c9c9cc;
  --canvas:#eef0f3;
  --white:#ffffff;
}
*{box-sizing:border-box;margin:0;padding:0}
html,body{width:1200px;height:5146px;overflow:hidden;background:var(--canvas);font-family:"Poppins",Arial,sans-serif;color:var(--ink)}
.page{position:absolute;left:25px;top:3px;width:1000px;height:4470px;transform:scale(1.15);transform-origin:0 0;background:var(--white);overflow:hidden}
.bands{position:absolute;left:0;top:0}
.abs{position:absolute}
.center{left:0;width:1000px;text-align:center}
.logo{font-weight:700;color:var(--white);letter-spacing:-.5px}
.nav{display:flex;gap:22px;font-size:9px;color:#f3d5d8}
.btn{display:inline-block;font-size:9px;font-weight:600;padding:7px 14px;border-radius:3px;color:var(--white)}
.btn-red{background:var(--red)}
.btn-navy{background:var(--navy)}
.btn-ghost{background:var(--white);color:var(--grey);border:1px solid var(--silver);border-radius:4px;font-weight:500;padding:5px 14px;font-size:8px}
.hero-line{font-size:27px;font-weight:300;color:var(--white);line-height:1.2}
.hero-key{font-size:28px;font-weight:700;line-height:1.2}
.red-heading{color:var(--red);font-weight:600;font-size:26px;line-height:1.38}
.body{font-size:13px;line-height:1.7;color:var(--ink)}
.small{font-size:9.5px;line-height:1.9;color:var(--grey)}
.photo{box-shadow:0 6px 18px rgba(40,10,15,.25)}
.ring{border:5px solid var(--white)}
.pill-card{background:var(--white);border-radius:3px;display:flex;align-items:center;gap:14px;padding:0 14px;height:60px;width:168px;box-shadow:0 2px 6px rgba(0,0,0,.15)}
.pill-card .num{font-size:16px;font-weight:500}
.pill-card .label{font-size:11px;line-height:1.25}
.client{width:108px;height:108px;border-radius:50%;background:var(--white);display:flex;align-items:center;justify-content:center;font-size:13px;font-weight:600;color:var(--red)}
.tabs{background:var(--white);box-shadow:0 2px 10px rgba(0,0,0,.1)}
.tab{display:flex;align-items:center;gap:10px;height:32px;padding:0 12px;font-size:9.5px;color:var(--ink)}
.tab i{width:12px;height:12px;border-radius:50%;border:1.5px solid var(--red)}
.tab.active{background:var(--red);color:var(--white)}
.tab.active i{border-color:var(--white)}
.feature{background:var(--white);border-radius:10px;text-align:center}
.feature h3{color:var(--red);font-size:15px;font-weight:600;line-height:1.35}
.foot-col{font-size:9px;line-height:1.75;color:#f6dfe1}
.foot-col h4{color:#e7626f;font-weight:500;font-size:10px}
.social{width:18px;height:18px;border-radius:50%;background:var(--red);border:1px solid #f2a3ab}
</style>
</head>
<body>
<main class="page">

<svg class="bands" width="1000" height="4470" viewBox="0 0 1000 4470" aria-hidden="true">
  <defs>
    <linearGradient id="redg" x1="0" y1="0" x2="1" y2="1">
      <stop offset="0" stop-color="#a50c1c"/><stop offset=".5" stop-color="#c8102e"/><stop offset="1" stop-color="#8a0b17"/>
    </linearGradient>
    <linearGradient id="mist" x1="0" y1="0" x2="1" y2="1">
      <stop offset="0" stop-color="#eef3ff"/><stop offset=".5" stop-color="#ffffff"/><stop offset="1" stop-color="#fde8ee"/>
    </linearGradient>
  </defs>
  <rect width="1000" height="4470" fill="url(#mist)"/>
  <path d="M0 0H1000V380C820 580 430 560 0 380Z" fill="#c2c2c6"/>
  <path d="M0 0H1000V360C820 560 430 540 0 360Z" fill="url(#redg)"/>
  <path d="M0 330C300 250 600 280 1000 140" stroke="#d8263d" stroke-width="40" fill="none" opacity=".35"/>
  <!-- hero accent blob -->
  <path d="M640 140C720 90 860 110 900 180C940 260 880 360 790 380C700 400 620 330 610 260C600 200 600 165 640 140Z" fill="#e0142f"/>
  <path d="M0 1290C350 1250 700 1230 1000 1250V1600C700 1560 350 1570 0 1600Z" fill="#c2c2c6"/>
  <path d="M0 1305C350 1265 700 1245 1000 1265V1590C700 1545 350 1555 0 1590Z" fill="url(#redg)"/>
  <path d="M0 2000C350 1970 700 1955 1000 1970V2370C700 2420 350 2430 0 2420Z" fill="url(#redg)"/>
  <path d="M0 1985C350 1955 700 1940 1000 1955V1972C700 1957 350 1972 0 2002Z" fill="#c2c2c6"/>
  <path d="M0 2920C350 2880 700 2880 1000 2900V3770C700 3730 300 3740 0 3780Z" fill="#c2c2c6"/>
  <path d="M0 2935C350 2895 700 2895 1000 2915V3760C700 3720 300 3730 0 3770Z" fill="url(#redg)"/>
  <path d="M0 4120C300 4050 700 4050 1000 4110V4470H0Z" fill="url(#redg)"/>
  <!-- dotted connectors -->
  <path d="M910 3120V3180" stroke="#fff" stroke-width="1.5" stroke-dasharray="2 3"/>
  <circle cx="910" cy="3114" r="5" fill="none" stroke="#fff"/>
  <path d="M800 3720H880" stroke="#888" stroke-width="1.5" stroke-dasharray="2 3"/>
  <circle cx="886" cy="3720" r="5" fill="none" stroke="#888"/>
  <circle cx="614" cy="3490" r="5" fill="none" stroke="#888"/>
</svg>

<!-- header -->
<div class="abs logo" style="left:126px;top:20px;font-size:20px">Lumora.io</div>
<nav class="abs nav" style="left:450px;top:32px">
  <span>Platform ›</span><span>Solutions ›</span><span>Resources ›</span><span>About</span><span>Pricing Plans</span>
</nav>
<span class="abs btn btn-red" style="left:780px;top:26px;box-shadow:0 0 0 1px #f08a95">Book a Demo</span>

<!-- hero -->
<div class="abs" style="left:126px;top:106px">
  <div class="hero-key" style="color:var(--green)">Reach</div>
  <div class="hero-line">the unreachable.</div>
  <div class="hero-key" style="color:var(--yellow);margin-top:22px">Engage</div>
  <div class="hero-line">the disengaged.</div>
  <div class="hero-key" style="color:var(--lime);margin-top:22px">Connect</div>
  <div class="hero-line">the unconnected.</div>
</div>
<div class="abs photo" role="img" aria-label="Modern office lounge with grey sofas and city windows" style="left:700px;top:104px;width:200px;height:200px;border-radius:50%;background:radial-gradient(circle at 40% 30%,#d6dbe2,#8d96a3 45%,#3e4753 90%)"></div>
<div class="abs photo" role="img" aria-label="Wall screen showing a financial report dashboard with three gauges" style="left:496px;top:170px;width:250px;height:150px;border-radius:3px;border:2px solid #e7e9ec;background:linear-gradient(150deg,#c7263a 0%,#a10f22 55%,#7d0b18 100%)"></div>

<!-- problem -->
<div class="abs center red-heading" style="top:604px">You know you have a problem.<br>We know why you have a problem.</div>
<div class="abs center" style="top:694px;font-size:14px;font-weight:500;text-decoration:underline">Let's solve it together.</div>
<div class="abs center" style="top:746px"><span class="btn btn-ghost">Read More ●</span></div>
<p class="abs center body" style="top:792px">Lumora enables you to bridge the communication gap and develop<br>a more informed, aligned and inspired workplace.</p>
<div class="abs center" style="top:862px"><span class="btn btn-red">Book a Demo</span>&nbsp;&nbsp;&nbsp;<span class="btn btn-navy">Watch Video</span></div>
<div class="abs" role="img" aria-label="Set of workplace screens, laptop, tablet and phone showing colourful comms content" style="left:240px;top:926px;width:480px;height:184px;border-radius:6px;background:radial-gradient(ellipse at 25% 45%,#f2b33d 0%,#c8102e 22%,rgba(40,44,60,.95) 48%),radial-gradient(ellipse at 80% 40%,#4fa3d9,#1e2a48 60%);background-blend-mode:screen;box-shadow:0 10px 22px rgba(0,0,0,.2)"></div>
<p class="abs center" style="top:1130px;font-size:10.5px;line-height:1.8">Comms teams can easily create and deliver content to all kinds of screens in<br>a vibrant, compelling and memorable format.</p>

<!-- teams -->
<div class="abs pill-card" style="left:126px;top:1350px"><span class="num" style="color:var(--red)">01</span><span class="label">Manage the<br>Culture</span></div>
<div class="abs pill-card" style="left:318px;top:1350px"><span class="num" style="color:#2f6fb3">02</span><span class="label">Calm the<br>Noise</span></div>
<div class="abs" style="left:510px;top:1350px;width:172px;height:150px;background:var(--white);border-radius:3px;padding:14px;box-shadow:0 2px 6px rgba(0,0,0,.15)">
  <div style="display:flex;gap:10px;align-items:center"><span style="font-size:16px;color:#2b8f8c">03</span><span style="font-size:11px;line-height:1.25">Change<br>Behaviour</span><span style="margin-left:auto;width:18px;height:18px;border-radius:50%;background:var(--red)"></span></div>
  <p style="font-size:7.5px;line-height:1.6;color:var(--grey);margin-top:10px">You can more easily ensure communication uptake and influence outcomes by carefully sequencing the delivery – the right messages at the right time.</p>
</div>
<div class="abs pill-card" style="left:700px;top:1350px"><span class="num" style="color:#c9a41a">04</span><span class="label">Inspire &amp;<br>Excite</span></div>
<div class="abs pill-card" style="left:126px;top:1440px"><span class="num" style="color:#3a9a3f">05</span><span class="label">Empower<br>Teams</span></div>
<div class="abs pill-card" style="left:318px;top:1440px"><span class="num" style="color:var(--yellow)">06</span><span class="label">Organisation<br>al Glue</span></div>
<div class="abs pill-card" style="left:700px;top:1440px"><span class="num">08</span><span class="label">Frontline to<br>Backoffice</span></div>

<!-- platform -->
<div class="abs red-heading" style="left:126px;top:1668px;font-size:24px;line-height:1.3">Lumora is the one workplace comms<br>platform that reaches &amp; engages<br>everyone, everywhere.</div>
<div class="abs" style="left:126px;top:1792px;font-size:14px;font-weight:600;line-height:1.5">Transform how you connect with<br>hard-to-reach workers.</div>
<p class="abs small" style="left:126px;top:1842px;font-size:10px;color:var(--ink)">Lumora brings together digital workplace screens, desktops<br>and mobiles to reach all your people – whether they're at<br>home at their desks, on the road or the factory floor.</p>
<div class="abs photo ring" role="img" aria-label="Circle of colourful content screens from the template library" style="left:700px;top:1640px;width:250px;height:250px;border-radius:50%;background:conic-gradient(from 30deg,#2f7d55,#d2463a,#f0b43c,#3f6fb5,#1f2b3f,#2f7d55)"></div>
<div class="abs photo" role="img" aria-label="Smiling man in a purple shirt holding a laptop" style="left:600px;top:1700px;width:150px;height:190px;border-radius:48% 48% 10px 10px;background:linear-gradient(180deg,#e7d7c9 0%,#8a63c4 45%,#5b3d98 100%)"></div>

<!-- clients -->
<div class="abs center" style="top:2056px;color:var(--white);font-size:24px;font-weight:500;line-height:1.35">Lumora works for large, complex<br>businesses and it will work for you, too.</div>
<svg class="abs" style="left:96px;top:2192px" width="12" height="16" aria-hidden="true"><path d="M9 2L3 8L9 14" stroke="#fff" stroke-width="1.5" fill="none"/></svg>
<svg class="abs" style="left:890px;top:2192px" width="12" height="16" aria-hidden="true"><path d="M3 2L9 8L3 14" stroke="#fff" stroke-width="1.5" fill="none"/></svg>
<div class="abs client" style="left:126px;top:2146px">Northway</div>
<div class="abs client" style="left:254px;top:2146px">Tidecrest</div>
<div class="abs client" style="left:382px;top:2146px">Kiwora</div>
<div class="abs client" style="left:510px;top:2146px">Elmcare</div>
<div class="abs client" style="left:638px;top:2146px">Orinda</div>
<div class="abs client" style="left:772px;top:2146px">Hillgate</div>
<div class="abs" style="left:252px;top:2276px;color:#ff2a3d;font-size:60px;font-weight:700;line-height:1">”</div>
<p class="abs" style="left:312px;top:2288px;color:var(--white);font-size:11px;line-height:1.6">Lorem Ipsum is simply dummy text of the printing and typesetting<br>industry. Lorem Ipsum has been the industry's standard – Kiwora</p>
<div class="abs center" style="top:2358px"><span class="btn btn-red" style="box-shadow:0 0 0 1px #f08a95">Book a Demo</span>&nbsp;&nbsp;&nbsp;<span class="btn btn-navy">Free Trial</span></div>

<!-- single platform -->
<div class="abs center red-heading" style="top:2492px;font-size:24px">A single platform for all your key teams.</div>
<div class="abs tabs" style="left:166px;top:2560px;width:220px">
  <div class="tab active"><i></i>Internal Communications</div>
  <div class="tab"><i></i>Health &amp; Safety</div>
  <div class="tab"><i></i>Operations</div>
  <div class="tab"><i></i>Learning &amp; Development</div>
  <div class="tab"><i></i>People &amp; Culture</div>
  <div class="tab"><i></i>IT &amp; Cybersecurity</div>
  <div class="tab"><i></i>Senior Leadership</div>
</div>
<div class="abs" style="left:436px;top:2596px;font-size:14px;font-weight:600;line-height:1.45">Lumora works for Internal<br>Communications teams</div>
<p class="abs small" style="left:436px;top:2648px;color:var(--ink)">Always pushed for time, often stretched for resources and<br>people. Lumora takes a huge load off internal comms teams,<br>transforming top-down messaging into high-quality visual<br>content, and automating production, delivery and sequencing.</p>
<span class="abs btn btn-navy" style="left:436px;top:2738px">Learn More</span>

<!-- features -->
<div class="abs feature" style="left:126px;top:3150px;width:364px;height:280px;padding-top:84px">
  <h3>Transform the way you connect with<br>hard-to-reach workers.</h3>
  <p class="small" style="margin-top:12px">Lumora brings together digital workplace screens,<br>desktop screens and mobiles to reach all of your<br>people, whether they're at home, at their desks, on the<br>road or the factory floor.</p>
  <span class="btn btn-ghost" style="margin-top:14px">Read More</span>
</div>
<div class="abs photo ring" role="img" aria-label="Site worker in a hi-vis vest and hard hat checking an incident dashboard" style="left:178px;top:2966px;width:260px;height:260px;border-radius:50%;background:linear-gradient(160deg,#c61a2c 0%,#8f1a24 38%,#f08a2a 60%,#3b4250 100%)"></div>
<div class="abs feature" style="left:510px;top:3150px;width:366px;height:280px;padding-top:84px">
  <h3>No need to play graphic<br>designer.</h3>
  <p class="small" style="margin-top:12px">Lumora gives you access to an extensive library<br>of templates, for effortless creation of<br>stunning content.</p>
  <span class="btn btn-ghost" style="margin-top:34px">Read More</span>
</div>
<div class="abs" role="img" aria-label="Woman at a laptop under a fan of colourful template thumbnails" style="left:556px;top:2976px;width:290px;height:200px;border-radius:8px;background:radial-gradient(ellipse at 50% 85%,#f1e4d6 0%,#d9c3ad 30%,transparent 55%),linear-gradient(170deg,#d13a3a 0%,#f0b43c 30%,#3a88c4 55%,rgba(255,255,255,0) 75%)"></div>
<div class="abs feature" style="left:126px;top:3480px;width:750px;height:240px"></div>
<div class="abs" style="left:126px;top:3526px;width:400px;text-align:center">
  <h3 style="color:var(--red);font-size:15px;font-weight:600;line-height:1.35">Bite-sized content for<br>snackable learning.</h3>
  <p class="small" style="margin-top:10px">Lumora's snackable learning framework delivers<br>messages that are optimally sized and sequenced for<br>uptake and retention.</p>
  <span class="btn btn-ghost" style="margin-top:14px">Read More</span>
</div>
<div class="abs photo ring" role="img" aria-label="Two colleagues discussing a cyber security tip shown on a wall screen" style="left:506px;top:3446px;width:300px;height:280px;border-radius:50%;background:linear-gradient(120deg,#e9dccd 0%,#c7a98c 30%,#2f7f86 58%,#1f3b4a 100%)"></div>

<!-- call to action -->
<div class="abs center red-heading" style="top:3864px;font-size:24px">Transform the way you talk to<br>your workforce.</div>
<div class="abs center" style="top:3944px;font-size:13px">Lumora will enable you to reach &amp; engage everyone, everywhere.</div>
<div class="abs center" style="top:3990px"><span class="btn btn-red">Book a Demo</span>&nbsp;&nbsp;&nbsp;<span class="btn btn-navy">Find our More</span></div>

<!-- footer -->
<div class="abs center logo" style="top:4160px;font-size:30px">Lumora.io</div>
<div class="abs foot-col" style="left:126px;top:4226px"><h4>Lumora.io</h4>Platform Overview<br>Features<br>Security<br>Workplace Digital Signage Screens<br>Corporate Screensavers<br>Template Library<br>Integrations<br>Infotainment Streams<br>Premium Programs</div>
<div class="abs foot-col" style="left:338px;top:4226px"><h4>Who we're for</h4>Industrial &amp; Manufacturing<br>Mining &amp; Construction<br>Government &amp; Public Sector<br>Aged Care<br>Logistics<br>Retail</div>
<div class="abs foot-col" style="left:524px;top:4226px"><h4>Resources</h4>Latest Insights<br>Snackable Learning Framework<br>Help Centre<br>Server Status<br>Privacy Policy<br>Terms &amp; Service</div>
<div class="abs foot-col" style="left:716px;top:4226px"><h4>Get started</h4>Book a Demo<br>Free Trial<br>Pricing<br>Become a Partner<br>Contact Us</div>
<div class="abs" style="left:126px;top:4424px;font-size:8.5px;color:#f6dfe1">© 2024 Lumora.io Limited All rights reserved</div>
<div class="abs social" style="left:802px;top:4420px"></div>
<div class="abs social" style="left:828px;top:4420px"></div>
<div class="abs social" style="left:856px;top:4420px"></div>

</main>
</body>
</html>
```